Brochure Design Project (Design Studio)

Items required:
1-Brochure. We suggest 15Cm X 15 Cm after cutting.
2-Business Card.
3-Head letter.
4-Folder ( folder should carry the Brochure in pocket and the business card in a pocket on the opposite side of the folder.
5-Envelope to carry everything.
This brochure is expected to draw attention of high level management in companies to the quality and creativity of the design work and encourage them to do business with us. note that brochure will be printed in high quality printing and paper.
The game plan is as follows:
Over all description, the theme of the brochure is drawn from the website theme (website will be uploaded shortly, pictures of the website are attached, logo appears in the top left corner). Please avoid direct copying from the website unless it is a creative copying, just draw the theme from there. however, we need it to be elegant, stylish and class in colors and style. This is a MUST.
Furthermore, the main items of the Brochure:
1-The Studio is not just a studio: we will take about how Branding. A file is attached of the content. (slight changes/modification can apply during the designing process)
2-The Process: this one has to be a visual illustration of the process, it has to be very creative, could be elegant arrows and comics, could be elegant drawing, could be an elegant icons. The drawing should be separate from the steps, we need to the drawing and we need to have the steps listed and commentary, or if want to integrate both in one in an artistic way. Just don’t lose track of the theme and elegance. (steps and commentary are attached, slight changes/modification can apply at anytime.
3-Our Team: another drawing of your suggestion to illustrate the team members, we need to include the names and designation as well leave a place for some of them to say what they need to say about their style of designing. I leave it for your imagination to put this all together in a nice attractive visual illustration.
4-Works: this section will generally show the works of our designers. It needs to be focused on the works themselves, client should be able to view the details of the works ( note that when it comes to brochures and websites, we don’t need to reach to the extent with which the client can read the text in those pictures of the website or brochure, but still can see the overall design clearly). Each design is to carry the name of the designer. Last thing, this section will classify works into categories, like, Brochures, Corporate identity, print design. We didn’t finalize those categories, we will provide them to you shortly, last thing to be said, we are planning to include around 25-30 designs of each sub-category, eg. Corporate identity will have 30 business card s designs and 30 stationary designs.
5-Contacts: the company contacts.
We the brochure after printing should be 15x15 Cm.
Creativity and art work is a major player in selection.
general managers, owners
Printing

```html
<!DOCTYPE html>
<html lang="en">
<head>
<meta charset="utf-8">
<title>The Process – Brochure Spread</title>
<link href="https://fonts.googleapis.com/css2?family=Dancing+Script:wght@600&family=Roboto:wght@100;300;400&display=swap" rel="stylesheet">
<style>
  :root {
    --page-bg: #ffffff;
    --spread-bg: #000000;
    --band: #b7bd72;
    --band-text: #8e934e;
    --accent: #b9c46c;
    --text: #ffffff;
    --oval-light: #b3c06a;
    --oval-dark: #4b5820;
    --oval-label: #111111;
  }
  * { box-sizing: border-box; margin: 0; padding: 0; }
  html, body { width: 1200px; height: 900px; overflow: hidden; background: var(--page-bg); }
  body { position: relative; font-family: "Roboto", Arial, sans-serif; color: var(--text); }

  .spread { position: absolute; left: 50px; top: 175px; width: 1100px; height: 550px; background: var(--spread-bg); }
  .spread > * { position: absolute; }

  .colour-strip { left: 5px; top: 52px; width: 227px; height: 14px;
    background: linear-gradient(90deg, #1a2540, #6d87a8, #2b3a55, #9fb0c4, #44546a, #c9cdb8, #7d8f6f, #e0dcc0, #8b7a58, #c79a5a, #3a3020, #b66a2a, #e08a3a); }

  .section-title { left: 265px; top: 34px; font-family: "Dancing Script", cursive; font-weight: 600; font-size: 38px; color: var(--accent); }

  .step { font-size: 12.6px; line-height: 15.6px; font-weight: 300; }
  .step p + p { margin-top: 10px; }
  .badge { float: left; width: 90px; height: 50px; margin-right: 2px; position: relative; }
  .badge svg { position: absolute; left: 0; top: -14px; overflow: visible; }
  .oval-label { font-family: "Roboto", Arial, sans-serif; font-size: 7.6px; fill: var(--oval-label); }
  .step-number { font-family: "Roboto", Arial, sans-serif; font-weight: 100; fill: var(--text); }

  .step-brainstorm { left: 53px; top: 123px; width: 216px; }
  .step-technical { left: 286px; top: 123px; width: 214px; }
  .step-concepts  { left: 286px; top: 285px; width: 214px; }
  .step-selection { left: 598px; top: 115px; width: 225px; }
  .step-execution { left: 843px; top: 115px; width: 150px; }

  .flow-diagram { left: 570px; top: 255px; overflow: visible; }
  .flow-title { left: 838px; top: 282px; font-size: 22px; font-weight: 300; }
  .tagline { left: 582px; top: 410px; width: 200px; font-size: 15.6px; line-height: 19.5px; font-weight: 300; }

  .footer-band { left: 0; top: 513px; width: 1100px; height: 37px; background: var(--band); }
  .footer-mark { top: 524px; font-size: 10px; letter-spacing: 1px; color: var(--band-text); }
  .footer-mark .studio { font-weight: 400; }
  .footer-left { left: 358px; }
  .footer-right { left: 908px; }
</style>
</head>
<body>
<svg width="0" height="0" aria-hidden="true" style="position:absolute">
  <defs>
    <linearGradient id="ovalFill" x1="0" y1="0" x2="1" y2="0">
      <stop offset="0" stop-color="var(--oval-light)"/>
      <stop offset="1" stop-color="var(--oval-dark)"/>
    </linearGradient>
    <marker id="arrowHead" viewBox="0 0 10 10" refX="6" refY="5" markerWidth="5" markerHeight="5" orient="auto">
      <path d="M0 0 L10 5 L0 10 Z" fill="#fff"/>
    </marker>
  </defs>
</svg>

<main class="spread">
  <div class="colour-strip" role="img" aria-label="Decorative strip of thin vertical colour bars"></div>
  <h1 class="section-title">The Process</h1>

  <section class="step step-brainstorm">
    <div class="badge"><svg width="90" height="62">
      <text class="step-number" x="2" y="55" font-size="58">1</text>
      <ellipse cx="44" cy="39" rx="43" ry="18" fill="url(#ovalFill)" stroke="#fff" stroke-width="2.5"/>
      <text class="oval-label" x="44" y="42" text-anchor="middle">Braistorming</text></svg></div>
    <p>We identify the objectives of the design. We aim to identify the ultimate perception to be made among customers. We as well tap on the challenges faced by our customers including competitive force.</p>
    <p>We don’t compromise on understanding the client requirements at a core level in order to see the mission of creating any particular design from the client’s eyes not ours!</p>
  </section>

  <section class="step step-technical">
    <div class="badge"><svg width="90" height="62">
      <text class="step-number" x="0" y="58" font-size="58">2</text>
      <ellipse cx="46" cy="42" rx="42" ry="19" fill="url(#ovalFill)" stroke="#fff" stroke-width="2.5"/>
      <text class="oval-label" x="46" y="40" text-anchor="middle">Build technical</text>
      <text class="oval-label" x="46" y="50" text-anchor="middle">description</text></svg></div>
    <p>Creative Manager builds a technical description of client’s requirements which translates the requirements to designing language. And then the job is dispatched to designers.</p>
  </section>

  <section class="step step-concepts">
    <div class="badge"><svg width="90" height="62">
      <text class="step-number" x="2" y="58" font-size="58">3</text>
      <ellipse cx="44" cy="42" rx="42" ry="19" fill="url(#ovalFill)" stroke="#fff" stroke-width="2.5"/>
      <text class="oval-label" x="46" y="40" text-anchor="middle">Produce many</text>
      <text class="oval-label" x="46" y="50" text-anchor="middle">concept desogns</text></svg></div>
    <p>Each designer produces visual composition based on his understanding of the requirements. Clients expect 5-10 different ideas for their requirements according to different styles of designing.</p>
    <p>Our business concept guarantees the maximum level of creativity in generating ideas.</p>
  </section>

  <section class="step step-selection">
    <div class="badge"><svg width="90" height="62">
      <text class="step-number" x="2" y="58" font-size="58">4</text>
      <ellipse cx="44" cy="42" rx="43" ry="19" fill="url(#ovalFill)" stroke="#fff" stroke-width="2.5"/>
      <text class="oval-label" x="46" y="40" text-anchor="middle">Selection and</text>
      <text class="oval-label" x="46" y="50" text-anchor="middle">implementation</text></svg></div>
    <p>All Concept mockups are passed to client to select best one. The selected design is revised several times with client till client is ultimately satisfied with the results.</p>
  </section>

  <section class="step step-execution">
    <div class="badge"><svg width="90" height="62">
      <text class="step-number" x="2" y="58" font-size="58">5</text>
      <ellipse cx="44" cy="42" rx="43" ry="19" fill="url(#ovalFill)" stroke="#fff" stroke-width="2.5"/>
      <text class="oval-label" x="46" y="45" text-anchor="middle">Execution</text></svg></div>
    <p>Final design is sent for printing and execution.</p>
  </section>

  <svg class="flow-diagram" width="580" height="260" viewBox="570 255 580 260" aria-label="Five process steps joined by arrows">
    <g fill="none" stroke="#fff" stroke-width="2.5" marker-end="url(#arrowHead)">
      <path d="M667 283 Q730 270 745 328"/>
      <path d="M770 327 Q835 312 850 370"/>
      <path d="M875 357 Q940 347 952 402"/>
      <path d="M978 395 Q1045 382 1057 440"/>
    </g>
    <g stroke="#fff" stroke-width="2.5">
      <ellipse cx="622" cy="306" rx="43" ry="19" fill="url(#ovalFill)"/>
      <ellipse cx="715" cy="360" rx="43" ry="19" fill="url(#ovalFill)"/>
      <ellipse cx="819" cy="403" rx="43" ry="19" fill="url(#ovalFill)"/>
      <ellipse cx="922" cy="435" rx="43" ry="19" fill="url(#ovalFill)"/>
      <ellipse cx="1035" cy="475" rx="43" ry="19" fill="url(#ovalFill)"/>
    </g>
    <g class="step-number" font-size="50">
      <text x="578" y="318">1</text><text x="670" y="371">2</text><text x="774" y="414">3</text><text x="877" y="447">4</text><text x="990" y="486">5</text>
    </g>
    <text class="oval-label" x="622" y="309" text-anchor="middle">Braistorming</text>
    <text class="oval-label" x="719" y="357" text-anchor="middle">Build technical</text>
    <text class="oval-label" x="719" y="367" text-anchor="middle">description</text>
    <text class="oval-label" x="823" y="400" text-anchor="middle">Produce many</text>
    <text class="oval-label" x="823" y="410" text-anchor="middle">concept desogns</text>
    <text class="oval-label" x="926" y="432" text-anchor="middle">Selection and</text>
    <text class="oval-label" x="926" y="442" text-anchor="middle">implementation</text>
    <text class="oval-label" x="1039" y="478" text-anchor="middle">Execution</text>
  </svg>

  <h2 class="flow-title">The Process</h2>
  <p class="tagline">We are more than just a creative studio; we can personify your business and dress to impress!</p>

  <div class="footer-band"></div>
  <p class="footer-mark footer-left"><span class="studio">Verdant Studio</span> | since 2009</p>
  <p class="footer-mark footer-right"><span class="studio">Verdant Studio</span> | since 2009</p>
</main>
</body>
</html>
```